Vell Studio - Lash Serum Packaging

Need Packaging done for this Lash Serum for a brand called "Vell Studio". The bottle will remain black but the box can be any color. This will be for a 3ml bottle. Give me different options for packaging that is minimalist and clean for this brand that makes it look expensive and make people want to buy.

```html
<!DOCTYPE html>
<html lang="en">
<head>
<meta charset="utf-8">
<title>Vell Studio – Lash &amp; Brown Serum Labels</title>
<link href="https://fonts.googleapis.com/css2?family=Montserrat:wght@400;500&display=swap" rel="stylesheet">
<style>
  :root{
    --paper:#ffffff;
    --label:#151413;
    --gold:#d8b869;
    --ink:#1c1c1c;
    --shadow:rgba(0,0,0,.35);
  }
  *{margin:0;padding:0;box-sizing:border-box}
  html,body{width:1200px;height:677px;overflow:hidden;background:var(--paper)}
  body{position:relative;font-family:"Montserrat",sans-serif;color:var(--ink)}

  .dimensions{position:absolute;left:0;top:0;width:1200px;height:677px}
  .dim-text{font-family:"Montserrat",sans-serif;font-size:10px;fill:var(--ink)}

  .label{position:absolute;background:var(--label);box-shadow:6px 5px 7px var(--shadow)}
  .label-box{left:455px;top:130px;width:135px;height:487px}
  .label-serum{left:656px;top:337px;width:74px;height:293px}

  .brand{position:absolute;color:var(--gold);font-weight:500;white-space:nowrap;line-height:1}
  .label-box .brand{left:15px;top:58px;font-size:15px;letter-spacing:.04em}
  .label-serum .brand{left:12px;top:248px;font-size:8px;letter-spacing:.04em}

  .gold-rule{position:absolute;left:17px;top:88px;width:1px;height:232px;background:var(--gold)}

  .product-name{position:absolute;color:var(--gold);font-weight:400;text-transform:uppercase}
  .label-box .product-name{left:14px;top:335px;font-size:16.5px;letter-spacing:.38em;line-height:22px}
  .label-serum .product-name{left:10px;top:38px;font-size:8px;letter-spacing:.34em;line-height:10px;padding-bottom:3px;border-bottom:1px solid var(--gold)}

  .volume{position:absolute;left:46px;top:449px;width:43px;height:11px;border-radius:6px;background:var(--gold);color:var(--label);font-size:8px;font-weight:500;letter-spacing:.25em;text-align:center;line-height:11px;padding-left:2px}

  .caption{position:absolute;top:638px;font-size:19px;font-weight:400;color:var(--ink);transform:translateX(-50%);white-space:nowrap}
  .caption-box{left:507px}
  .caption-serum{left:704px}
</style>
</head>
<body>
  <svg class="dimensions" viewBox="0 0 1200 677" aria-hidden="true">
    <defs>
      <marker id="arrow" viewBox="0 0 10 10" refX="9" refY="5" markerWidth="7" markerHeight="7" orient="auto-start-reverse">
        <path d="M0 1 L10 5 L0 9 z" fill="#1c1c1c"/>
      </marker>
    </defs>
    <g stroke="#1c1c1c" stroke-width=".6" fill="none">
      <!-- box width -->
      <line x1="455" y1="45" x2="455" y2="124"/>
      <line x1="590" y1="45" x2="590" y2="124"/>
      <line x1="456" y1="52" x2="589" y2="52" stroke-width="1" marker-start="url(#arrow)" marker-end="url(#arrow)"/>
      <!-- serum width -->
      <line x1="656" y1="45" x2="656" y2="332"/>
      <line x1="730" y1="45" x2="730" y2="332"/>
      <line x1="657" y1="52" x2="729" y2="52" stroke-width="1" marker-start="url(#arrow)" marker-end="url(#arrow)"/>
      <!-- box height -->
      <line x1="403" y1="130" x2="452" y2="130"/>
      <line x1="403" y1="617" x2="452" y2="617"/>
      <line x1="411" y1="131" x2="411" y2="616" stroke-width="1" marker-start="url(#arrow)" marker-end="url(#arrow)"/>
      <!-- serum height -->
      <line x1="732" y1="337" x2="793" y2="337"/>
      <line x1="732" y1="630" x2="793" y2="630"/>
      <line x1="786" y1="338" x2="786" y2="629" stroke-width="1" marker-start="url(#arrow)" marker-end="url(#arrow)"/>
    </g>
    <text class="dim-text" x="522" y="44" text-anchor="middle">5,84 cm</text>
    <text class="dim-text" x="693" y="44" text-anchor="middle">3,09 cm</text>
    <text class="dim-text" transform="translate(403 374) rotate(-90)" text-anchor="middle">20,24 cm</text>
    <text class="dim-text" transform="translate(801 483) rotate(-90)" text-anchor="middle">12,19 cm</text>
  </svg>

  <div class="label label-box">
    <div class="brand">Vell Studio</div>
    <div class="gold-rule"></div>
    <div class="product-name">Lash<br>&amp;<br>Brown<br>Serum</div>
    <div class="volume">3ml</div>
  </div>

  <div class="label label-serum">
    <div class="product-name">Lash<br>&amp;<br>Brown<br>Serum</div>
    <div class="brand">Vell Studio</div>
  </div>

  <div class="caption caption-box">label box</div>
  <div class="caption caption-serum">label serum</div>
</body>
</html>
```